Direct Response Landing Page for Paid Search Campaigns for TrailKeepers.com

TrailKeepers.com is a leading people search / public records company, providing consumers with instant, accurate access to public records. We are a direct response org focused on engaging the user and converting the user to a customer. Our product returns instant search results based on a name or phone search. We are looking for a landing page to test out, against our current "Home Page." We will drive traffic to this page via paid search terms (ie., "people search, find people"). We would like a landing page with a headline, search forms, CTA Search button, with features/beneifts about the service and company. Specific Key Messaging will be provided.

Target Market(s)

Consumers. Skew slightly female, ages 40+

Industry/Entity Type

It Company

Number of Pages Required

1 page

Font styles to use
Sans Serif

Requirements
Must have
• Use of Logo; upper left corner, consistent w/ TrailKeepers.com.
• Use of two HTML search forms (prefer a toggle between the two). Users must type in a search query in a search form for either:
• 1. First Name, Last Name, City, State
• 2. Phone # (area code w/ phone #)
• Call to Action: "Search" button
Should not have
• Should not include TrailKeepers.com's standard nav at the top.

```html
<!DOCTYPE html>
<html lang="en">
<head>
<meta charset="utf-8">
<title>TrailKeepers.com – People Search</title>
<link href="https://fonts.googleapis.com/css2?family=Cabin:ital,wght@0,400;0,500;0,600;1,400;1,500&display=swap" rel="stylesheet">
<style>
:root{
  --page-bg:#e6e6e6;
  --sheet:#f0f0f0;
  --header-top:#e2e2e2;
  --header-bottom:#f7f7f7;
  --brand-blue:#2a7fc0;
  --brand-green:#2f9a4a;
  --accent-plum:#8c2a63;
  --menu-grey:#5b5b5b;
  --link-blue:#2a7fc0;
  --link-red:#d9342b;
  --banner-green:#63b77b;
  --teal:#5bbfca;
  --rule:#8fd0d8;
  --text-dark:#333;
  --text-mid:#444;
  --cta:#e8481c;
  --tab-active:#2585cf;
  --tab-idle:#8fb6dc;
  --input-bg:#e2e2e2;
  --input-border:#9a9a9a;
  --dot-dark:#3a3a3a;
}
*{margin:0;padding:0;box-sizing:border-box}
html,body{width:965px;height:1200px;overflow:hidden}
body{background:var(--page-bg);font-family:"Cabin",sans-serif;color:var(--text-dark);position:relative}
.sheet{position:absolute;left:64px;top:0;width:835px;height:1200px;background:var(--sheet)}
.abs{position:absolute}
.header{left:64px;top:0;width:835px;height:105px;background:linear-gradient(var(--header-top),var(--header-bottom));box-shadow:0 4px 6px rgba(0,0,0,.25)}
.brand{left:86px;top:26px;display:flex;align-items:center;gap:8px}
.brand-mark{width:40px;height:40px;border-radius:50%;background:var(--brand-blue)}
.brand-name{font-size:34px;font-weight:400;color:var(--brand-blue);letter-spacing:-.5px}
.account-links{right:86px;top:30px;font-size:9.5px;color:var(--link-blue)}
.account-links span{color:#aaa;margin:0 3px}
.signup{right:86px;top:45px;font-size:8px;color:var(--link-red);display:flex;align-items:center;gap:4px}
.menu{right:86px;top:84px;display:flex;gap:13px;font-size:13px;font-weight:600;color:var(--menu-grey)}
.menu .current{color:var(--accent-plum);margin-right:6px}
.menu-pointer{left:582px;top:105px;width:0;height:0;border-left:7px solid transparent;border-right:7px solid transparent;border-top:7px solid var(--header-bottom)}
.hero-banner{left:256px;top:139px;width:454px;height:76px;background:var(--banner-green);border:1px solid #58a96e;border-radius:2px;color:#fff;text-align:center}
.hero-banner h1{font-weight:400;font-size:24px;margin-top:10px}
.hero-banner p{font-size:16px;margin-top:1px}
.start-here{left:86px;top:239px;font-size:12px;color:var(--brand-green);display:flex;align-items:center;gap:4px}
.search-panel{left:88px;top:262px;width:791px;height:173px;background:linear-gradient(#1d5f8a 10%,#2f7a8c 45%,#5db57d 100%);border:1px solid #4a8fb0}
.search-tabs{height:24px;background:var(--tab-active);display:flex}
.tab{font-size:11.5px;font-weight:600;color:#fff;padding:0 11px;line-height:24px}
.tab.active{background:#1f79c5;width:110px}
.tab.idle{background:var(--tab-idle);color:#d9e8f5}
.field{position:absolute;top:79px;width:176px;height:30px;background:var(--input-bg);border:1px solid var(--input-border);border-radius:2px;font-size:13px;font-weight:500;color:#8a8a8a;padding:6px 9px}
.field .chev{position:absolute;right:5px;top:5px;width:18px;height:18px;background:#f4f4f4;border:1px solid #999}
.btn-search{position:absolute;left:677px;top:130px;width:90px;height:27px;background:var(--cta);color:#fff;font-size:11.5px;font-weight:600;text-align:center;line-height:27px;border-radius:2px}
.section-title{font-size:19px;font-weight:500;color:var(--teal);text-align:center}
.rule{height:1px;background:var(--rule)}
.illus-network{left:207px;top:494px;width:113px;height:93px;background:radial-gradient(circle,#3f8fd0 0%,#7fb3d8 45%,#cfd8df 75%,rgba(240,240,240,0) 100%)}
.facts{left:420px;top:510px;font-size:12px;font-style:italic;color:var(--text-dark)}
.facts li{list-style:none;display:flex;align-items:center;gap:8px;height:22px}
.help-col{width:170px;text-align:center;font-size:9.6px;font-style:italic;font-weight:500;line-height:18.5px;color:var(--text-dark)}
.partner{top:861px;width:78px;height:51px;background:#fff;display:flex;align-items:center;justify-content:center;text-align:center;font-size:9px;font-weight:600;color:#333;padding:3px;line-height:11px}
.dot{width:11px;height:11px;border-radius:50%;background:#fff;border:1px solid #ddd}
.avatar{left:226px;top:991px;width:109px;height:109px;background:linear-gradient(#c4c4c4,#d0d0d0)}
.quote{left:418px;top:1010px;width:380px;font-size:12px;line-height:19px;color:var(--text-mid)}
.quote-by{right:86px;top:1096px;font-size:9px;font-weight:500;color:var(--text-mid)}
.t-dot{width:11px;height:11px;border-radius:50%;background:var(--dot-dark)}
.footer-note{left:86px;top:1172px;width:793px;text-align:center;font-size:16px;color:var(--teal)}
</style>
</head>
<body>
<div class="sheet"></div>

<header class="abs header"></header>
<div class="abs brand"><span class="brand-mark"></span><span class="brand-name">trailkeepers</span></div>
<div class="abs account-links">My Account<span>|</span>My Reports<span>|</span>Log in</div>
<div class="abs signup">Sign up for a Membership
  <svg width="10" height="10" viewBox="0 0 10 10"><circle cx="5" cy="5" r="4.3" fill="none" stroke="#d9342b" stroke-width="1"/><path d="M4 3l2.2 2L4 7" fill="none" stroke="#d9342b" stroke-width="1.1"/></svg>
</div>
<nav class="abs menu"><span class="current">MENU ONE</span><span>MENU TWO</span><span>MENU THREE</span><span>MENU FOUR</span></nav>
<div class="abs menu-pointer"></div>

<section class="abs hero-banner">
  <h1>TrailKeepers.com</h1>
  <p>Since 1999, Your Trusted Online People Search Source</p>
</section>

<div class="abs start-here">
  <svg width="11" height="11" viewBox="0 0 11 11"><circle cx="5.5" cy="5.5" r="4.8" fill="none" stroke="#2f9a4a" stroke-width="1.2"/><path d="M4.3 3.3l2.6 2.2-2.6 2.2z" fill="#2f9a4a"/></svg>
  Start Here – Enter in a Name to Begin
</div>

<form class="abs search-panel">
  <div class="search-tabs"><span class="tab active">Search by Name</span><span class="tab idle">Search by Phone</span></div>
  <div class="field" style="left:20px">First Name</div>
  <div class="field" style="left:209px">Last Name</div>
  <div class="field" style="left:400px">City</div>
  <div class="field" style="left:590px">Select State
    <span class="chev"><svg width="16" height="16" viewBox="0 0 16 16"><path d="M3 5.5l5 5 5-5" fill="none" stroke="#555" stroke-width="1.6"/></svg></span>
  </div>
  <div class="btn-search">Search</div>
</form>

<div class="abs rule" style="left:88px;top:474px;width:300px"></div>
<div class="abs rule" style="left:568px;top:474px;width:312px"></div>
<h2 class="abs section-title" style="left:388px;top:461px;width:180px">Who We Are</h2>
<div class="abs illus-network" role="img" aria-label="Illustration of a globe surrounded by people on jigsaw puzzle pieces"></div>
<ul class="abs facts">
  <li><svg width="18" height="18" viewBox="0 0 18 18"><circle cx="9" cy="9" r="8" fill="none" stroke="#2a7fc0" stroke-width="1.3"/><path d="M5.5 6.5h7M5.5 9h7M5.5 11.5h7" stroke="#2a7fc0" stroke-width="1.2"/></svg>Launched online in 1999</li>
  <li><svg width="18" height="18" viewBox="0 0 18 18"><circle cx="9" cy="9" r="8" fill="none" stroke="#2a7fc0" stroke-width="1.3"/><rect x="5.5" y="5" width="7" height="8" fill="none" stroke="#2a7fc0" stroke-width="1.2"/></svg>Leading Data-as-a-Service Public Records Organization</li>
  <li><svg width="18" height="18" viewBox="0 0 18 18"><circle cx="9" cy="9" r="8" fill="none" stroke="#2a7fc0" stroke-width="1.3"/><rect x="6" y="8.5" width="6" height="4.5" fill="#2a7fc0"/><path d="M7 8.5V7a2 2 0 014 0v1.5" fill="none" stroke="#2a7fc0" stroke-width="1.2"/></svg>Privacy and Security are paramount to our Organization</li>
</ul>

<div class="abs rule" style="left:88px;top:634px;width:300px"></div>
<div class="abs rule" style="left:568px;top:634px;width:312px"></div>
<h2 class="abs section-title" style="left:388px;top:621px;width:180px">How We Help</h2>

<svg class="abs" style="left:150px;top:653px" width="38" height="38" viewBox="0 0 38 38"><rect width="38" height="38" fill="#1f3f8f"/><circle cx="19" cy="19" r="13" fill="none" stroke="#fff" stroke-width="2"/><text x="19" y="24" font-family="Cabin,sans-serif" font-size="14" font-weight="600" fill="#fff" text-anchor="middle">$</text></svg>
<p class="abs help-col" style="left:84px;top:694px">TrailKeepers has people, phone, background, property and criminal, at your fingertips.</p>

<svg class="abs" style="left:470px;top:653px" width="38" height="40" viewBox="0 0 38 40"><path d="M14 4h10l-3 6h-4z" fill="#222"/><path d="M17 10h4c9 4 14 13 14 20 0 6-6 9-16 9S3 36 3 30c0-7 5-16 14-20z" fill="#222"/><text x="19" y="33" font-family="Cabin,sans-serif" font-size="15" font-weight="600" fill="#fff" text-anchor="middle">$</text></svg>
<p class="abs help-col" style="left:404px;top:694px">We do the vetting for you to access local, state and nationwide records + delivering you AFFORDABLE UNLIMITED access</p>

<svg class="abs" style="left:792px;top:653px" width="38" height="38" viewBox="0 0 38 38"><rect width="38" height="38" fill="#3a8fd6"/><rect x="6" y="12" width="16" height="20" fill="none" stroke="#fff" stroke-width="2"/><rect x="16" y="6" width="16" height="26" fill="none" stroke="#fff" stroke-width="2"/></svg>
<p class="abs help-col" style="left:726px;top:692px">We Provide Instant Access to Billions of People Search &amp; Background Records.</p>

<div class="abs rule" style="left:86px;top:822px;width:277px"></div>
<div class="abs rule" style="left:609px;top:822px;width:270px"></div>
<h2 class="abs section-title" style="left:363px;top:809px;width:246px">Who we've worked with</h2>

<div class="abs partner" style="left:84px">Halvern Broadcast</div>
<div class="abs partner" style="left:186px">Marlow &amp; Finch</div>
<div class="abs partner" style="left:288px">Greyhaven Council</div>
<div class="abs partner" style="left:390px">Invest Eastmoor</div>
<div class="abs partner" style="left:492px">Corrin City Council</div>
<div class="abs partner" style="left:594px">Valeside Care</div>
<div class="abs partner" style="left:696px">Morning Ledger</div>
<div class="abs partner" style="left:798px">Arts Forum</div>

<div class="abs dot" style="left:793px;top:943px;background:#8a8a8a;border-color:#8a8a8a"></div>
<div class="abs dot" style="left:817px;top:943px"></div>
<div class="abs dot" style="left:840px;top:943px"></div>
<div class="abs dot" style="left:864px;top:943px"></div>

<div class="abs rule" style="left:88px;top:969px;width:297px"></div>
<div class="abs rule" style="left:581px;top:969px;width:298px"></div>
<h2 class="abs section-title" style="left:385px;top:955px;width:196px">What Client’s Say</h2>

<div class="abs avatar" role="img" aria-label="Client portrait placeholder"></div>
<p class="abs quote">Lorem ipsum dolor sit amet, consectetur adipiscing elit. Curabitur non bibendum leo. Ut blandit in leo sit amet pharetra. nibh tellus efficitur magna, at blandit nibh ligula eu mi. Suspendisse fermentum, nisl eget accumsan posuere,</p>
<p class="abs quote-by">Lorem ipsum dolor sit amet</p>

<div class="abs t-dot" style="left:418px;top:1119px"></div>
<div class="abs t-dot" style="left:440px;top:1119px"></div>
<div class="abs t-dot" style="left:462px;top:1119px"></div>
<div class="abs t-dot" style="left:484px;top:1119px;background:var(--teal)"></div>
<div class="abs t-dot" style="left:506px;top:1119px"></div>
<div class="abs t-dot" style="left:528px;top:1119px"></div>
<div class="abs t-dot" style="left:550px;top:1119px"></div>

<div class="abs rule" style="left:88px;top:1161px;width:791px"></div>
<footer class="abs footer-note">Your footer will be placed here</footer>
</body>
</html>
```